Business Card

Can you please copy the format provided for the business cards.
Can the logo be in the colours of the last file as specified.

Can the text please be in grey

• Navy Blue: #00457C
• Grey Text: #555555
• Orange Text: #FDBF29

The names on the business card will be

Dorian Pike
0455 718 302
dorian.pike@tallowridgeleasing.example.au

Lvl 7, 14 Harlow Pde
Merrivale QLD 4388
PO Box 3412
Sunhaven MC QLD 9812
P: 1300 742 619
F: 1300 742 638
www.tallowridgeleasing.example.au

And

Leon Whitcombe
0467 590 148
leon.whitcombe@tallowridgeleasing.example.au

Lvl 7, 14 Harlow Pde
Merrivale QLD 4388
PO Box 3412
Sunhaven MC QLD 9812
P: 1300 742 619
F: 1300 743 905

```html
<!DOCTYPE html>
<html lang="en">
<head>
<meta charset="utf-8">
<title>Tallow Ridge Leasing – Business Cards</title>
<link rel="stylesheet" href="https://fonts.googleapis.com/css2?family=Lato:wght@400;700&display=swap">
<style>
  :root {
    --navy: #00457C;
    --grey-text: #555555;
    --orange: #FDBF29;
    --card: #ffffff;
    --backdrop: #5b2c18;
    --rule: #9a9a9a;
  }
  * { margin: 0; padding: 0; box-sizing: border-box; }
  html, body {
    width: 1200px;
    height: 926px;
    overflow: hidden;
  }
  body {
    background: var(--backdrop);
    font-family: "Lato", Arial, sans-serif;
    position: relative;
  }
  .card {
    position: absolute;
    width: 508px;
    height: 328px;
    background: var(--card);
    overflow: hidden;
  }
  .card--front-a { left: 80px;  top: 110px; }
  .card--back-a  { left: 625px; top: 110px; }
  .card--front-b { left: 80px;  top: 478px; }
  .card--back-b  { left: 625px; top: 478px; }

  .brand {
    position: absolute;
    display: flex;
    align-items: center;
    gap: 12px;
  }
  .brand__mark {
    width: 44px;
    height: 44px;
    background: var(--navy);
    flex: none;
  }
  .brand__name {
    color: var(--navy);
    font-weight: 700;
    font-size: 19px;
    line-height: 1.05;
    letter-spacing: 0.3px;
  }
  .card--front-a .brand, .card--front-b .brand { left: 36px; top: 64px; }

  .brand--small { gap: 9px; }
  .brand--small .brand__mark { width: 32px; height: 32px; }
  .brand--small .brand__name { font-size: 14px; }
  .card--back-a .brand, .card--back-b .brand { left: 30px; top: 150px; }

  .tagline {
    position: absolute;
    right: 37px;
    top: 80px;
    text-align: right;
    font-weight: 700;
    font-size: 19px;
    line-height: 1.15;
    color: var(--grey-text);
  }
  .tagline__accent-navy { color: var(--navy); }
  .tagline__accent-orange { color: var(--orange); }

  .contact {
    position: absolute;
    left: 39px;
    top: 220px;
    color: var(--grey-text);
  }
  .contact__name { font-size: 23px; font-weight: 700; line-height: 1.2; }
  .contact__phone { font-size: 20px; line-height: 1.25; }
  .contact__email { font-size: 14px; line-height: 1.6; }

  .office {
    position: absolute;
    left: 196px;
    top: 96px;
    padding-left: 10px;
    border-left: 1px solid var(--rule);
    color: var(--grey-text);
    font-size: 15px;
    font-style: normal;
    line-height: 20px;
  }
</style>
</head>
<body>

  <section class="card card--front-a">
    <div class="brand">
      <span class="brand__mark"></span>
      <span class="brand__name">TALLOW RIDGE<br>LEASING</span>
    </div>
    <p class="tagline">Lease <span class="tagline__accent-navy">Smarter</span><br>Grow <span class="tagline__accent-orange">Steadier</span></p>
    <div class="contact">
      <p class="contact__name">Dorian Pike</p>
      <p class="contact__phone">0455 718 302</p>
      <p class="contact__email">dorian.pike@tallowridgeleasing.example.au</p>
    </div>
  </section>

  <section class="card card--back-a">
    <div class="brand brand--small">
      <span class="brand__mark"></span>
      <span class="brand__name">TALLOW RIDGE<br>LEASING</span>
    </div>
    <address class="office">
      Lvl 7, 14 Harlow Pde<br>
      Merrivale QLD 4388<br>
      PO Box 3412<br>
      Sunhaven MC QLD 9812<br>
      P: 1300 742 619<br>
      F: 1300 742 638<br>
      www.tallowridgeleasing.example.au
    </address>
  </section>

  <section class="card card--front-b">
    <div class="brand">
      <span class="brand__mark"></span>
      <span class="brand__name">TALLOW RIDGE<br>LEASING</span>
    </div>
    <p class="tagline">Lease <span class="tagline__accent-navy">Smarter</span><br>Grow <span class="tagline__accent-orange">Steadier</span></p>
    <div class="contact">
      <p class="contact__name">Leon Whitcombe</p>
      <p class="contact__phone">0467 590 148</p>
      <p class="contact__email">leon.whitcombe@tallowridgeleasing.example.au</p>
    </div>
  </section>

  <section class="card card--back-b">
    <div class="brand brand--small">
      <span class="brand__mark"></span>
      <span class="brand__name">TALLOW RIDGE<br>LEASING</span>
    </div>
    <address class="office">
      Lvl 7, 14 Harlow Pde<br>
      Merrivale QLD 4388<br>
      PO Box 3412<br>
      Sunhaven MC QLD 9812<br>
      P: 1300 742 619<br>
      F: 1300 743 905<br>
      www.tallowridgeleasing.example.au
    </address>
  </section>

</body>
</html>
```